Food Safety 1-California workers only

3.25" by 4.5" Black and White Magazine Ad
This ad is to train California workers only.
Workers will be trained on: Food Safety, FSMA (Food Safety Modernization Act), using equipment safety, food processing production skills, worker safety, supervisory skills, communication skills.
"FREE TRAINING", The company does the training or Keystone Learning will provide the training.
Training grants range from $100,000 to $400,000.
Companies must be in business for profit.
Companies must train 200 employees or more.
This program is for California workers only.
Incumbent or new-hires are eligible.

Target Market(s)

California food processors, farms, food packaging, food processors, companies under FSMA, food safety, food production who need to train employees.

Industry/Entity Type

Food Production

Font styles to use
Serif
Sans Serif

Colors

Designer to choose colors to be used in the design.

Requirements
Must have
• This is a 3.25 inch by 4.5 inch magazine ad. It must be black and white. No color.
• The deliverable must be in basic PhotoShop. The ad does not need to include any graphics and be text only if needed. If you have a black and white graphic that will show well.
• Look at www.KLGFoodSafety..com
• Use the text from "MEALBOX-Photoshop-052018" file as your starting point.
Nice to have
• A black and white graphic about food. See www.KLGFoodSafety.com
Should not have
• No color.

```html
<!DOCTYPE html>
<html lang="en">
<head>
<meta charset="utf-8">
<title>Free Training Food Safety – Keystone Learning</title>
<link href="https://fonts.googleapis.com/css2?family=Roboto+Slab:wght@300;400;700;800&family=Arimo:wght@400;700&display=swap" rel="stylesheet">
<style>
  :root{
    --ink:#000;
    --paper:#fff;
    --backdrop:#a7a8aa;
    --rule:#9a9a9a;
  }
  *{margin:0;padding:0;box-sizing:border-box}
  html,body{width:909px;height:1200px;overflow:hidden;background:var(--backdrop)}
  .ad{position:absolute;left:134px;top:157px;width:641px;height:886px;background:var(--paper);overflow:hidden;isolation:isolate;font-family:"Arimo",Arial,sans-serif;color:var(--ink)}
  .ad > *{position:absolute;white-space:nowrap;line-height:1}
  .slab{font-family:"Roboto Slab",Georgia,serif}
  .invert{color:var(--paper);mix-blend-mode:difference}

  .top-band{left:0;top:0;width:641px;height:58px;background:var(--ink)}
  .headline-free{left:40px;top:26px;font-size:66px;font-weight:800;transform:scaleX(1.02);transform-origin:left}
  .headline-training{left:283px;top:26px;font-size:66px;font-weight:300;letter-spacing:-1px}
  .headline-topic{left:40px;top:88px;font-size:76px;font-weight:700;letter-spacing:-1px;transform:scaleX(1.06);transform-origin:left}

  .topic{left:0;width:641px;text-align:center;font-size:23px}
  .topic-fsma{top:162px}
  .topic-skills{top:188px}
  .rule-bar{top:216px;height:17px;background:var(--ink)}
  .rule-left{left:41px;width:126px}
  .rule-right{left:471px;width:127px}
  .topic-safety{top:213px;left:170px;width:300px;text-align:center;font-size:22px;font-weight:700}

  .map-area{left:42px;top:248px;width:212px;height:256px;background:var(--ink)}

  .pitch-you{left:150px;top:254px;font-size:44px;font-weight:800}
  .pitch-do{left:256px;top:256px;font-size:64px;font-weight:800}
  .pitch-the{left:368px;top:256px;font-size:24px;font-weight:700}
  .pitch-training{left:368px;top:282px;font-size:30px;font-weight:700}
  .pitch-andthe{left:365px;top:316px;font-size:11px;font-weight:700}
  .pitch-state{left:293px;top:322px;font-size:34px;font-weight:800}
  .pitch-of{left:416px;top:342px;font-size:10px;font-weight:700}
  .pitch-state-name{left:88px;top:348px;font-size:84px;font-weight:800;letter-spacing:-2px;transform:scaleX(1.03);transform-origin:left}
  .pitch-pays{left:262px;top:424px;font-size:96px;font-weight:800;letter-spacing:-2px}
  .pitch-for{left:498px;top:430px;font-size:38px;font-weight:700}
  .pitch-it{left:498px;top:463px;font-size:38px;font-weight:700}

  .qualify-bar{left:41px;top:507px;width:557px;height:26px;background:var(--ink);color:var(--paper);font-size:18px;font-weight:700;text-align:center;padding-top:4px}
  .qualify-list{left:56px;top:541px;list-style:none;font-size:19px}
  .qualify-list li{height:24.5px;padding-left:18px;position:relative}
  .qualify-list li::before{content:"";position:absolute;left:0;top:6px;width:6px;height:6px;background:var(--ink)}

  .footer-band{left:0;top:750px;width:641px;height:136px;background:var(--ink)}
  .contact-title{left:0;top:718px;width:641px;text-align:center;font-size:40px;font-weight:800}
  .footer-text{left:0;width:641px;text-align:center;color:var(--paper)}
  .contact-name{top:757px;font-size:19px;font-weight:700}
  .contact-address{top:782px;font-size:15px}
  .contact-suite{top:806px;font-size:15px}
  .footer-rule{top:811px;height:1px;background:var(--rule)}
  .footer-rule-left{left:56px;width:137px}
  .footer-rule-right{left:447px;width:137px}
  .contact-web{top:828px;font-size:20px}
  .contact-mail{top:853px;font-size:18px}
  .contact-mail b{font-weight:700}
</style>
</head>
<body>
<main class="ad">
  <div class="top-band"></div>
  <div class="headline-free slab invert">FREE</div>
  <div class="headline-training slab invert">TRAINING</div>
  <div class="headline-topic slab">FOOD SAEFTY</div>

  <div class="topic topic-fsma">FSMA</div>
  <div class="topic topic-skills">PRODUCTION SKILLS</div>
  <div class="rule-bar rule-left"></div>
  <div class="rule-bar rule-right"></div>
  <div class="topic-safety">WORKERS SAFETY</div>

  <div class="map-area" role="img" aria-label="Black silhouette map of the state of California"></div>

  <div class="pitch-you slab invert">YOU</div>
  <div class="pitch-do slab invert">DO</div>
  <div class="pitch-the slab invert">THE</div>
  <div class="pitch-training slab invert">TRAINING</div>
  <div class="pitch-andthe slab invert">AND THE</div>
  <div class="pitch-state slab invert">STATE</div>
  <div class="pitch-of slab invert">OF</div>
  <div class="pitch-state-name slab invert">CALIFORNIA</div>
  <div class="pitch-pays slab invert">PAYS</div>
  <div class="pitch-for slab invert">FOR</div>
  <div class="pitch-it slab invert">IT!</div>

  <div class="qualify-bar">HOW TO QUALIFY:</div>
  <ul class="qualify-list">
    <li>Train California Workers Only.</li>
    <li>Trainees must earn $11/hour</li>
    <li>Full-time workers only.</li>
    <li>Employees must attend at least 8 Hours or training</li>
    <li>You must train 200 or more employees</li>
    <li>Incumbent or New-Hire workers are eligible</li>
    <li>Seasonal workers are eligible</li>
  </ul>

  <div class="footer-band"></div>
  <div class="contact-title slab invert">CONTACT</div>
  <div class="footer-text contact-name">DANIEL HARTWELL</div>
  <div class="footer-text contact-address">KEYSTONE LEARNING COMPANY, INC., 1200 HARBOR CREST DRIVE</div>
  <div class="footer-rule footer-rule-left"></div>
  <div class="footer-text contact-suite">SUITE 310, IRVINE, CA 92618,</div>
  <div class="footer-rule footer-rule-right"></div>
  <div class="footer-text contact-web">WWW.KLGCAL.COM | WWW.KLGFOODSAFETY.COM</div>
  <div class="footer-text contact-mail">E-MAIL:DAN.HARTWELL@KLGCAL.COM | PH.:<b>(949)555-0142</b></div>
</main>
</body>
</html>
```